Rebrand stationary with recently completed logo design

Need new business cards, thank you cards, letterhead, envelopes and presentation folders. The designs will be sent to a separate production firm so I need the files to be print ready.

My contact info
Reno Vaskelind

Office 604-381-4756
Fax 604-318-5064

Email reno@glazeworks.ca
website www.glazeworks.ca

315-27140 62nd Avenue,
Langley, BC, V3K 2R8

Target Market(s)

Homeowners, businesses and contractors

Industry/Entity Type

Business

Font styles to use
Sans Serif

Colors
34a7d7

Requirements
Must have
• Like to have one side of the business card a solid color with the logo in all white. The side with all the text to be a white background
• I find the current blue on the front of the card with the white logo too dark.
Should not have
• Gradient colors

```html
<!DOCTYPE html>
<html lang="en">
<head>
<meta charset="utf-8">
<title>Glazeworks Stationery</title>
<link rel="stylesheet" href="https://fonts.googleapis.com/css2?family=Open+Sans:wght@400;600&family=Great+Vibes&display=swap">
<style>
  :root {
    --brand-blue: #34a7d7;
    --ink: #3a3f45;
    --mark: #3d4248;
    --paper: #ffffff;
    --stage: #e6e7e9;
    --faint: #eef6fb;
    --rule: #e3e6ea;
  }
  * { box-sizing: border-box; margin: 0; padding: 0; }
  html, body { width: 1200px; height: 3600px; overflow: hidden; }
  body {
    background: var(--stage);
    font-family: "Open Sans", Arial, sans-serif;
    color: var(--ink);
    position: relative;
  }
  .sheet { position: absolute; background: var(--paper); overflow: hidden; box-shadow: 0 2px 6px rgba(0,0,0,.12); }
  .sheet--blue { background: var(--brand-blue); }

  /* brand lockup */
  .brand { position: absolute; display: flex; align-items: center; gap: 10px; }
  .brand__square { background: var(--mark); flex: none; }
  .brand__name { font-weight: 400; color: var(--brand-blue); letter-spacing: .04em; text-transform: uppercase; line-height: 1; }
  .brand--white .brand__name { color: var(--paper); }
  .brand--white .brand__square { background: var(--paper); }

  .faint-square { position: absolute; background: var(--faint); }
  .sheet--blue .faint-square { background: rgba(255,255,255,.14); }

  /* folder + letterhead */
  .folder { left: 150px; top: 90px; width: 420px; height: 580px; }
  .letterhead { left: 630px; top: 90px; width: 420px; height: 580px; }
  .letterhead__sender { position: absolute; right: 28px; top: 34px; font-size: 13px; }
  .letterhead__footer { position: absolute; left: 0; right: 0; bottom: 28px; text-align: center; font-size: 9px; line-height: 1.6; }
  .letterhead__footer b { color: var(--brand-blue); font-weight: 600; }

  /* business card */
  .card-back { left: 560px; top: 820px; width: 520px; height: 300px; }
  .card-front { left: 120px; top: 1000px; width: 520px; height: 300px; }
  .card-front__bar { position: absolute; left: 0; top: 34px; width: 12px; height: 40px; background: var(--mark); }
  .card-front__name { position: absolute; left: 34px; top: 40px; font-size: 22px; }
  .card-front__address { position: absolute; left: 34px; top: 96px; font-size: 15px; line-height: 1.4; }
  .card-front__contact { position: absolute; left: 34px; top: 168px; font-size: 15px; line-height: 1.4; }
  .card-front__contact b { color: var(--brand-blue); font-weight: 600; }

  /* envelopes */
  .envelope-back { left: 100px; top: 1420px; width: 1000px; height: 500px; }
  .envelope-back__strip { position: absolute; left: 0; top: 0; width: 100%; height: 24px; background: var(--brand-blue); }
  .envelope-back__flap { position: absolute; inset: 0; }
  .envelope-front { left: 100px; top: 2000px; width: 1000px; height: 500px; }
  .envelope-front__return { position: absolute; left: 0; right: 0; bottom: 22px; text-align: center; font-size: 15px; }

  /* thank you card */
  .thanks { left: 300px; top: 2860px; width: 600px; height: 380px; }
  .thanks__script { position: absolute; left: 0; right: 0; top: 110px; text-align: center; font-family: "Great Vibes", cursive; font-size: 82px; color: var(--ink); }
  .thanks__name { position: absolute; left: 30px; bottom: 26px; font-size: 19px; }
</style>
</head>
<body>

  <!-- Presentation folder -->
  <section class="sheet sheet--blue folder">
    <div class="faint-square" style="left:120px;top:40px;width:260px;height:460px;"></div>
    <div class="brand brand--white" style="left:80px;top:280px;">
      <span class="brand__square" style="width:22px;height:22px;"></span>
      <span class="brand__name" style="font-size:30px;">Glazeworks</span>
    </div>
  </section>

  <!-- Letterhead -->
  <section class="sheet letterhead">
    <div class="faint-square" style="left:180px;top:60px;width:220px;height:420px;"></div>
    <div class="brand" style="left:28px;top:30px;gap:6px;">
      <span class="brand__square" style="width:10px;height:10px;"></span>
      <span class="brand__name" style="font-size:14px;">Glazeworks</span>
    </div>
    <p class="letterhead__sender">Reno Vaskelind</p>
    <p class="letterhead__footer">
      315-27140 62nd Avenue, Langley, BC, V3K 2R8<br>
      <b>Office</b> : 604-381-4756 | <b>Fax</b> : 604-318-5064 | <b>Email</b> : reno@glazeworks.ca<br>
      www.glazeworks.ca
    </p>
  </section>

  <!-- Business card, logo side -->
  <section class="sheet sheet--blue card-back">
    <div class="faint-square" style="left:330px;top:30px;width:150px;height:250px;"></div>
    <div class="brand brand--white" style="left:110px;top:134px;">
      <span class="brand__square" style="width:24px;height:24px;"></span>
      <span class="brand__name" style="font-size:32px;">Glazeworks</span>
    </div>
  </section>

  <!-- Business card, text side -->
  <section class="sheet card-front">
    <div class="faint-square" style="left:360px;top:40px;width:130px;height:230px;"></div>
    <span class="card-front__bar"></span>
    <p class="card-front__name">Reno Vaskelind</p>
    <p class="card-front__address">315-27140 62nd Avenue,<br>Langley, BC, V3K 2R8</p>
    <p class="card-front__contact">
      <b>O.</b> 604-381-4756<br>
      <b>F.</b> 604-318-5064<br>
      <b>E.</b> reno@glazeworks.ca<br>
      www.glazeworks.ca
    </p>
    <div class="brand" style="left:300px;top:238px;gap:7px;">
      <span class="brand__square" style="width:14px;height:14px;"></span>
      <span class="brand__name" style="font-size:22px;">Glazeworks</span>
    </div>
  </section>

  <!-- Envelope, back -->
  <section class="sheet envelope-back">
    <div class="envelope-back__strip"></div>
    <svg class="envelope-back__flap" viewBox="0 0 1000 500" aria-hidden="true">
      <polyline points="0,24 500,300 1000,24" fill="none" stroke="var(--rule)" stroke-width="2"/>
      <line x1="0" y1="500" x2="380" y2="232" stroke="var(--rule)" stroke-width="2"/>
      <line x1="1000" y1="500" x2="620" y2="232" stroke="var(--rule)" stroke-width="2"/>
    </svg>
    <div class="brand" style="left:410px;top:110px;gap:7px;">
      <span class="brand__square" style="width:14px;height:14px;"></span>
      <span class="brand__name" style="font-size:22px;">Glazeworks</span>
    </div>
  </section>

  <!-- Envelope, front -->
  <section class="sheet envelope-front">
    <div class="faint-square" style="left:640px;top:40px;width:300px;height:380px;"></div>
    <div class="brand" style="left:30px;top:74px;gap:8px;">
      <span class="brand__square" style="width:18px;height:18px;"></span>
      <span class="brand__name" style="font-size:28px;">Glazeworks</span>
    </div>
    <p class="envelope-front__return">if undelivered, Please return to : 315-27140 62nd Avenue, Langley, BC, V3K 2R8</p>
  </section>

  <!-- Thank you card -->
  <section class="sheet thanks">
    <div class="faint-square" style="left:300px;top:0;width:240px;height:380px;"></div>
    <p class="thanks__script">Thank you</p>
    <p class="thanks__name">Reno Vaskelind</p>
    <div class="brand" style="left:370px;top:330px;gap:6px;">
      <span class="brand__square" style="width:12px;height:12px;"></span>
      <span class="brand__name" style="font-size:20px;">Glazeworks</span>
    </div>
  </section>

</body>
</html>
```